Package of web graphics needed

Utilizing a recently selected logo from a Loom Bazaar contest, we need to have some ads, fb cover, home page slide image created for our new 844-Toll-Free Number Product. Please feel free to check our site at www.marbleoakline.com

You'll find attached the 844 toll free logo in 2 layouts.

Here are the ads and dimensions of each that are needed:
1.)Banners/ads - 468x60
468×60 px
125×125 px
120×600 px
120x90 px
88×31 px button
5.)FB Cover - 851 x 315
6.)Home page slider image - 944 x 328

Here is the text & some ideas to use for these. Feel free to use different versions depending on which ad they work better on:
-

Market Your Business in a Memorable Way – Pre-Order Yours Today, Deadline: Dec. 7th
[include logo]
-
[844 logo] Don't Miss out on your chance to finally get a great vanity!

Order Yours Today
-

Don't Miss out on your chance to finally get a great vanity!
Dec. 7th Deadline to pre-order

Don't Ignore 844!– The newest toll free prefix – Coming Dec. 7th – Get Yours Today

FB COVER guidelines -
Requirements:
Include the logo
Limited Time Left – Get your Reservation in by December 7th

HOME PAGE Image Slide:
Use the logo,

Couple of Ideas we're interested in seeing:

[Billboard sign stock image … with the number 833-Grab-ONE on the billboard]
[844 logo and caricature] [1 caricature looking surprised]

Reason: Need more designs to review !

```html
<!DOCTYPE html>
<html lang="en">
<head>
<meta charset="utf-8">
<title>Dialnest Web Graphics Package</title>
<link rel="stylesheet" href="https://fonts.googleapis.com/css2?family=Montserrat:wght@400;500;600;700;800&family=PT+Sans+Narrow:wght@400;700&family=Kalam:wght@400&display=swap">
<style>
  :root {
    --board: #2b2c2a;
    --navy: #0f3466;
    --navy-deep: #0a2a55;
    --green: #5bb52a;
    --green-dark: #3f9a1c;
    --green-pale: #d8efb8;
    --lime: #a6d867;
    --white: #ffffff;
    --mist: #e8edf2;
    --sky: #2f8fe0;
    --sky-light: #bfe3fb;
  }
  * { margin: 0; padding: 0; box-sizing: border-box; }
  html, body { width: 1200px; height: 962px; overflow: hidden; }
  body { background: var(--board); position: relative; font-family: "Montserrat", sans-serif; }
  .ad { position: absolute; overflow: hidden; }
  .brand { font-family: "PT Sans Narrow", sans-serif; font-weight: 700; color: var(--navy); line-height: 1; white-space: nowrap; }
  .condensed { font-family: "PT Sans Narrow", sans-serif; }

  /* 125 x 125 */
  .ad-square { left: 192px; top: 87px; width: 125px; height: 125px; background: linear-gradient(160deg, var(--green-pale), var(--lime)); text-align: center; }
  .ad-square .brand { font-size: 30px; margin-top: 10px; }
  .ad-square .tagline { font-family: "PT Sans Narrow", sans-serif; color: var(--navy); font-size: 15px; line-height: 19px; margin-top: 10px; }
  .ad-square .footer { position: absolute; left: 0; bottom: 0; width: 100%; height: 28px; background: var(--navy); color: var(--white); font-family: "PT Sans Narrow", sans-serif; font-weight: 700; font-size: 15px; line-height: 28px; }

  /* 120 x 90 */
  .ad-small { left: 336px; top: 122px; width: 120px; height: 90px; background: linear-gradient(160deg, var(--green-pale), var(--lime)); text-align: center; }
  .ad-small .brand { font-size: 26px; margin-top: 10px; }
  .ad-small .tagline { font-family: "PT Sans Narrow", sans-serif; color: var(--navy); font-size: 14px; margin-top: 8px; }
  .ad-small .footer { position: absolute; left: 0; bottom: 0; width: 100%; height: 23px; background: var(--navy); color: var(--white); font-family: "PT Sans Narrow", sans-serif; font-weight: 700; font-size: 13px; line-height: 23px; }

  /* 88 x 31 */
  .ad-button { left: 493px; top: 91px; width: 88px; height: 31px; background: var(--lime); display: flex; align-items: center; justify-content: center; }
  .ad-button .brand { font-size: 19px; }

  /* 468 x 60 */
  .ad-leader { left: 485px; top: 152px; width: 468px; height: 60px; background: var(--white); border: 1px solid #cfd8c4; }
  .ad-leader .brand { position: absolute; left: 14px; top: 16px; font-size: 26px; }
  .ad-leader .pitch { position: absolute; left: 170px; top: 3px; width: 296px; height: 52px; background: linear-gradient(100deg, var(--lime), var(--green-pale)); clip-path: polygon(4% 0, 100% 0, 100% 100%, 0 100%); }
  .ad-leader .pitch p { position: absolute; left: 26px; top: 9px; font-family: "PT Sans Narrow", sans-serif; color: var(--navy); font-size: 14px; line-height: 19px; }
  .ad-leader .cta { position: absolute; right: 9px; top: 4px; width: 62px; height: 52px; background: var(--navy); color: var(--white); font-family: "PT Sans Narrow", sans-serif; font-size: 14px; line-height: 15px; text-align: center; padding-top: 4px; border: 1px solid var(--white); }

  /* 120 x 600 */
  .ad-sky { left: 1027px; top: 91px; width: 120px; height: 600px; background: linear-gradient(170deg, var(--green-pale), #c6e79c 60%, var(--green-pale)); }
  .ad-sky .head { position: absolute; left: 0; top: 0; width: 120px; height: 118px; background: var(--white); }
  .ad-sky .head .brand { position: absolute; left: 0; width: 120px; top: 58px; text-align: center; font-size: 26px; }
  .ad-sky .swoosh { position: absolute; left: 0; top: 104px; }
  .ad-sky .pitch { position: absolute; left: 11px; top: 152px; width: 104px; color: var(--navy); font-size: 16px; line-height: 24px; font-weight: 500; }
  .ad-sky .deadline { position: absolute; left: 11px; top: 333px; color: var(--navy); font-size: 16px; line-height: 24px; font-weight: 500; }
  .ad-sky .deadline .date { font-size: 20px; font-weight: 400; }
  .ad-sky .cta { position: absolute; left: 10px; top: 464px; width: 100px; height: 88px; background: var(--navy); border: 1px solid #5a7fb0; border-radius: 3px; color: var(--white); font-family: "PT Sans Narrow", sans-serif; font-weight: 700; font-size: 24px; line-height: 25px; text-align: center; padding-top: 6px; }
  sup { font-size: 0.55em; }

  /* FB cover 851 x 315 */
  .ad-cover { left: 50px; top: 244px; width: 851px; height: 315px; background: var(--green); }
  .ad-cover .skyline { position: absolute; left: 0; top: 107px; width: 851px; height: 208px; background: linear-gradient(180deg, var(--green) 0%, #4aa521 60%, var(--green-dark) 100%); }
  .ad-cover .bar { position: absolute; left: 0; top: 10px; width: 851px; height: 97px; background: linear-gradient(90deg, #54ae25, #4ea722); }
  .ad-cover .logo-box { position: absolute; left: 0; top: 10px; width: 387px; height: 97px; background: var(--white); display: flex; align-items: center; justify-content: center; }
  .ad-cover .logo-box .brand { font-size: 50px; }
  .ad-cover .headline { position: absolute; left: 428px; top: 29px; color: var(--white); font-size: 22px; line-height: 31px; font-weight: 400; }
  .ad-cover .urgency { position: absolute; left: 62px; top: 135px; width: 326px; height: 81px; background: var(--navy); color: var(--white); font-size: 24px; letter-spacing: 2px; line-height: 81px; text-align: center; font-weight: 400; }
  .ad-cover .reserve { position: absolute; left: 388px; top: 135px; width: 393px; height: 81px; background: var(--mist); color: var(--navy); padding: 12px 0 0 40px; font-size: 20px; line-height: 30px; }
  .ad-cover .reserve strong { font-size: 23px; font-weight: 600; letter-spacing: 1px; }

  /* Home slider 944 x 328 */
  .ad-slider { left: 50px; top: 589px; width: 944px; height: 328px; }
  .ad-slider .scene { position: absolute; inset: 0; background: linear-gradient(170deg, var(--sky) 0%, var(--sky-light) 45%, var(--sky) 100%); }
  .ad-slider .sign { position: absolute; left: 25px; top: 41px; width: 675px; height: 226px; background: linear-gradient(180deg, #ffffff, #eef1f4); border: 3px solid #c7ccd1; }
  .ad-slider .sign .brand { position: absolute; left: 26px; top: 30px; width: 404px; height: 141px; display: flex; align-items: center; justify-content: center; font-size: 92px; background: var(--white); }
  .ad-slider .call { position: absolute; left: 448px; top: 32px; font-size: 74px; font-weight: 800; line-height: 68px; color: var(--navy); letter-spacing: 1px; }
  .ad-slider .call .now { color: var(--green); display: block; }
  .ad-slider .slogan { position: absolute; left: 35px; top: 181px; color: var(--green); font-size: 20px; font-weight: 700; letter-spacing: 1.4px; }
  .ad-slider .logo-box { position: absolute; left: 742px; top: 38px; width: 166px; height: 116px; background: var(--white); display: flex; align-items: center; justify-content: center; }
  .ad-slider .logo-box .brand { font-size: 34px; }
  .ad-slider .cta { position: absolute; left: 746px; top: 166px; width: 162px; height: 71px; background: linear-gradient(180deg, #6cc23a, var(--green-dark)); border: 2px solid #d7f0c4; border-radius: 3px; color: var(--white); font-family: "PT Sans Narrow", sans-serif; font-weight: 700; font-size: 23px; line-height: 26px; text-align: center; padding-top: 8px; }
  .ad-slider .deadline { position: absolute; left: 758px; top: 248px; width: 150px; text-align: center; color: var(--white); font-family: "Kalam", cursive; font-size: 21px; line-height: 27px; }
</style>
</head>
<body>

  <section class="ad ad-square" aria-label="125 by 125 ad">
    <div class="brand">Dialnest</div>
    <p class="tagline">The newest<br>TOLL FREE prefix</p>
    <div class="footer">Coming Dec. 7th</div>
  </section>

  <section class="ad ad-small" aria-label="120 by 90 ad">
    <div class="brand">Dialnest</div>
    <p class="tagline">TOLL FREE prefix</p>
    <div class="footer">Coming Dec. 7th</div>
  </section>

  <section class="ad ad-button" aria-label="88 by 31 button">
    <div class="brand">Dialnest</div>
  </section>

  <section class="ad ad-leader" aria-label="468 by 60 banner">
    <div class="brand">Dialnest</div>
    <div class="pitch"><p>Don't Miss out on your chance<br>to finally get a great vanity!</p></div>
    <div class="cta">ORDER<br>YOURS<br>TODAY</div>
  </section>

  <section class="ad ad-sky" aria-label="120 by 600 skyscraper">
    <div class="head"><div class="brand">Dialnest</div></div>
    <svg class="swoosh" width="120" height="30" viewBox="0 0 120 30" aria-hidden="true">
      <path d="M0 10 Q60 24 120 6 L120 16 Q60 32 0 20 Z" fill="#0f3466"/>
    </svg>
    <p class="pitch">Don't Miss out on your chance to finally get a great vanity!</p>
    <p class="deadline"><span class="date">DEC. 7<sup>th</sup></span><br>Deadline to<br>pre-order</p>
    <div class="cta">ORDER<br>YOURS<br>TODAY</div>
  </section>

  <section class="ad ad-cover" aria-label="Facebook cover">
    <div class="skyline" role="img" aria-label="Faint green city skyline"></div>
    <div class="bar"></div>
    <div class="logo-box"><div class="brand">Dialnest</div></div>
    <p class="headline">Don't Miss out on your chance<br>to finally get a great vanity!</p>
    <div class="urgency">LIMITED TIME LEFT</div>
    <div class="reserve">Get your Reservation in by<br><strong>DECEMBER 7<sup>th</sup></strong></div>
  </section>

  <section class="ad ad-slider" aria-label="Home page slider">
    <div class="scene" role="img" aria-label="Billboard with spotlights against a blue sky and city skyline"></div>
    <div class="sign">
      <div class="brand">Dialnest</div>
      <div class="call">CALL<span class="now">NOW</span></div>
      <p class="slogan">MARKET YOUR BUSINESS IN A MEMORABLE WAY</p>
    </div>
    <div class="logo-box"><div class="brand">Dialnest</div></div>
    <div class="cta">ORDER YOURS<br>TODAY!</div>
    <p class="deadline">Deadline<br>December 7<sup>th</sup></p>
  </section>

</body>
</html>
```